Ridgeway Mortgage - Banner Ads for Re-Marketing Campaigns

Need a banner ad for a retargeting Campaign with Bright Tally.

We would like to incorporate our attached logo. Also would like to incorporate a call to action "Pre-Qualify for a home loan today" and a button to click. This banner is to encourage previous customers to come back to our website and submit information. It must look good on mobile and desktop.

Our website is RidgewayMortgage.com

Target Market(s)

Customers Seeking a Mortgage Loan

Industry/Entity Type

Mortgage

Requirements
Must have
• We would like the same basic design in the 4 sizes below.
• 728 pixels by 90 pixels leaderboard
• 300 by 250 medium rectangle
• 300 by 600 half page
• 320 by 100 mobile banner
Nice to have
• a Call to action, a button to click, animation
Should not have
• We are open.

```html
<!DOCTYPE html>
<html lang="en">
<head>
<meta charset="utf-8">
<title>Ridgeway Mortgage – Banner Set</title>
<link rel="stylesheet" href="https://fonts.googleapis.com/css2?family=Bebas+Neue&family=Lato:wght@400;700;900&display=swap">
<style>
  :root {
    --navy: #135f8c;
    --sky: #1f8fd6;
    --deep: #17689f;
    --sun: #ffd42e;
    --sun-dark: #f4b400;
    --ink: #1b1b1b;
    --paper: #ffffff;
    --mist: #e9e9e9;
  }
  html, body {
    margin: 0;
    width: 1200px;
    height: 1200px;
    overflow: hidden;
  }
  body {
    background: linear-gradient(180deg, #d3d3d3 0%, #f6f6f6 55%, #dcdcdc 100%);
    position: relative;
  }
  .banner {
    position: absolute;
    display: block;
    box-shadow: 0 2px 5px rgba(0,0,0,0.3);
  }
  .banner--rectangle { left: 95px; top: 325px; width: 429px; height: 357px; }
  .banner--leaderboard { left: 87px; top: 734px; width: 875px; height: 106px; }
  .banner--wide { left: 87px; top: 904px; width: 1041px; height: 128px; }
  .headline { font-family: "Bebas Neue", "Oswald", sans-serif; }
  .button-label { font-family: "Lato", Arial, sans-serif; font-weight: 900; fill: var(--ink); }
  .brand-name { font-family: "Lato", Arial, sans-serif; font-weight: 400; fill: var(--navy); letter-spacing: 1px; }
</style>
</head>
<body>

<!-- Medium rectangle -->
<svg class="banner banner--rectangle" viewBox="0 0 500 416" role="img" aria-label="Ridgeway Mortgage rectangle banner">
  <defs>
    <linearGradient id="paperFade" x1="0" y1="0" x2="0" y2="1">
      <stop offset="0" stop-color="#ffffff"/>
      <stop offset="0.6" stop-color="#ffffff"/>
      <stop offset="1" stop-color="#e6e6e6"/>
    </linearGradient>
    <linearGradient id="sunButton" x1="0" y1="0" x2="0" y2="1">
      <stop offset="0" stop-color="#ffdf45"/>
      <stop offset="1" stop-color="#f6b800"/>
    </linearGradient>
  </defs>
  <rect class="backdrop" width="500" height="416" fill="url(#paperFade)"/>
  <path class="swoosh-sun" fill="var(--sun)" d="M0,190 C90,130 220,110 330,100 C420,92 475,50 500,12 L500,30 C470,70 420,110 330,118 C220,125 100,150 0,200 Z"/>
  <path class="swoosh-navy" fill="var(--navy)" d="M0,200 C100,150 220,125 330,118 C420,110 470,70 500,30 L500,380 L460,380 C475,300 440,250 445,190 C450,150 470,125 485,105 C430,130 330,135 250,145 C150,158 60,180 0,205 Z"/>
  <rect class="footer-band" y="380" width="500" height="36" fill="var(--sky)"/>

  <circle class="brand-mark" cx="72" cy="66" r="22" fill="var(--sun)"/>
  <text class="brand-name" x="124" y="62" font-size="23">RIDGEWAY</text>
  <text class="brand-name" x="124" y="86" font-size="23">MORTGAGE</text>

  <text class="headline" x="92" y="219" font-size="58" fill="var(--ink)" textLength="310" lengthAdjust="spacingAndGlyphs">PRE-QUALIFY FOR</text>
  <text class="headline" x="92" y="273" font-size="58" fill="var(--deep)" textLength="314" lengthAdjust="spacingAndGlyphs">A HOME LOAN TODAY</text>

  <ellipse cx="248" cy="350" rx="150" ry="6" fill="rgba(0,0,0,0.18)"/>
  <rect class="cta-button" x="79" y="293" width="337" height="55" rx="27.5" fill="url(#sunButton)"/>
  <text class="button-label" x="247.5" y="327" font-size="21" text-anchor="middle" textLength="285" lengthAdjust="spacingAndGlyphs">RIDGEWAYMORTGAGE.COM</text>
</svg>

<!-- Leaderboard -->
<svg class="banner banner--leaderboard" viewBox="0 0 1021 123" role="img" aria-label="Ridgeway Mortgage leaderboard banner">
  <defs>
    <linearGradient id="paperFadeLb" x1="0" y1="0" x2="0" y2="1">
      <stop offset="0" stop-color="#ffffff"/>
      <stop offset="1" stop-color="#e4e4e4"/>
    </linearGradient>
    <linearGradient id="oceanLb" x1="0" y1="0" x2="0" y2="1">
      <stop offset="0" stop-color="#1f86c8"/>
      <stop offset="1" stop-color="#16629b"/>
    </linearGradient>
    <linearGradient id="sunButtonLb" x1="0" y1="0" x2="0" y2="1">
      <stop offset="0" stop-color="#ffdf45"/>
      <stop offset="1" stop-color="#f6b800"/>
    </linearGradient>
  </defs>
  <rect width="1021" height="123" fill="url(#paperFadeLb)"/>
  <path class="edge-sun" fill="var(--sun)" d="M0,0 L260,0 C310,0 340,40 360,80 C372,105 382,123 392,123 L0,123 Z"/>
  <path class="edge-navy" fill="var(--navy)" d="M0,0 L248,0 C298,0 328,40 348,80 C360,105 370,123 380,123 L0,123 Z"/>
  <path class="panel-ocean" fill="url(#oceanLb)" d="M0,0 L236,0 C286,0 316,40 336,80 C348,105 356,123 364,123 L0,123 Z"/>

  <path class="curve-sun" fill="none" stroke="var(--sun)" stroke-width="7" d="M630,126 C690,110 720,20 775,-3"/>
  <path class="curve-sky" fill="none" stroke="var(--sky)" stroke-width="3" d="M645,126 C700,112 728,25 780,-3"/>
  <path class="edge-sun" fill="var(--sun)" d="M895,0 L1021,0 L1021,123 C1010,123 995,95 975,62 C955,28 935,0 895,0 Z"/>
  <path class="panel-sky" fill="var(--sky)" d="M910,0 L1021,0 L1021,110 C1010,100 998,80 985,58 C968,28 948,0 910,0 Z"/>

  <text class="headline" x="47" y="63" font-size="38" fill="var(--sun)" textLength="210" lengthAdjust="spacingAndGlyphs">PRE-QUALIFY FOR</text>
  <text class="headline" x="47" y="97" font-size="34" fill="var(--paper)" textLength="210" lengthAdjust="spacingAndGlyphs">A HOME LOAN TODAY</text>

  <ellipse cx="512" cy="88" rx="135" ry="4" fill="rgba(0,0,0,0.18)"/>
  <rect class="cta-button" x="364" y="37" width="296" height="48" rx="24" fill="url(#sunButtonLb)"/>
  <text class="button-label" x="512" y="68" font-size="18" text-anchor="middle" textLength="250" lengthAdjust="spacingAndGlyphs">RIDGEWAYMORTGAGE.COM</text>

  <circle class="brand-mark" cx="772" cy="61" r="20" fill="var(--sun)"/>
  <text class="brand-name" x="818" y="57" font-size="21">RIDGEWAY</text>
  <text class="brand-name" x="818" y="79" font-size="21">MORTGAGE</text>
</svg>

<!-- Wide banner -->
<svg class="banner banner--wide" viewBox="0 0 1215 149" role="img" aria-label="Ridgeway Mortgage wide banner">
  <defs>
    <linearGradient id="paperFadeWd" x1="0" y1="0" x2="0" y2="1">
      <stop offset="0" stop-color="#ffffff"/>
      <stop offset="1" stop-color="#e4e4e4"/>
    </linearGradient>
    <linearGradient id="oceanWd" x1="0" y1="0" x2="0" y2="1">
      <stop offset="0" stop-color="#1f86c8"/>
      <stop offset="1" stop-color="#16629b"/>
    </linearGradient>
    <linearGradient id="sunButtonWd" x1="0" y1="0" x2="0" y2="1">
      <stop offset="0" stop-color="#ffdf45"/>
      <stop offset="1" stop-color="#f6b800"/>
    </linearGradient>
  </defs>
  <rect width="1215" height="149" fill="url(#paperFadeWd)"/>
  <path class="edge-sun" fill="var(--sun)" d="M0,0 L310,0 C368,0 404,48 428,97 C442,127 454,149 466,149 L0,149 Z"/>
  <path class="edge-navy" fill="var(--navy)" d="M0,0 L296,0 C354,0 390,48 414,97 C428,127 440,149 452,149 L0,149 Z"/>
  <path class="panel-ocean" fill="url(#oceanWd)" d="M0,0 L282,0 C340,0 376,48 400,97 C414,127 424,149 434,149 L0,149 Z"/>

  <path class="curve-sun" fill="none" stroke="var(--sun)" stroke-width="8" d="M750,152 C820,134 856,24 922,-4"/>
  <path class="curve-sky" fill="none" stroke="var(--sky)" stroke-width="3.5" d="M768,152 C834,136 866,30 928,-4"/>
  <path class="edge-sun" fill="var(--sun)" d="M1065,0 L1215,0 L1215,149 C1202,149 1184,115 1160,75 C1136,34 1112,0 1065,0 Z"/>
  <path class="panel-sky" fill="var(--sky)" d="M1083,0 L1215,0 L1215,133 C1202,121 1188,97 1172,70 C1152,34 1128,0 1083,0 Z"/>

  <text class="headline" x="55" y="74" font-size="46" fill="var(--sun)" textLength="252" lengthAdjust="spacingAndGlyphs">PRE-QUALIFY FOR</text>
  <text class="headline" x="55" y="118" font-size="42" fill="var(--paper)" textLength="252" lengthAdjust="spacingAndGlyphs">A HOME LOAN TODAY</text>

  <ellipse cx="610" cy="109" rx="160" ry="5" fill="rgba(0,0,0,0.18)"/>
  <rect class="cta-button" x="433" y="45" width="353" height="60" rx="30" fill="url(#sunButtonWd)"/>
  <text class="button-label" x="609.5" y="83" font-size="22" text-anchor="middle" textLength="296" lengthAdjust="spacingAndGlyphs">RIDGEWAYMORTGAGE.COM</text>

  <circle class="brand-mark" cx="918" cy="74" r="24" fill="var(--sun)"/>
  <text class="brand-name" x="974" y="69" font-size="25">RIDGEWAY</text>
  <text class="brand-name" x="974" y="96" font-size="25">MORTGAGE</text>
</svg>

</body>
</html>
```